Stationery for new photography studio
Flyer, Gift Certificate, Business Card, headed paper, CD label and case cover
Please note the change in email address
studio@brightferndesigns.at
Dear sir,
Thanks for your feedback.
#100 is brilliant
I really like #97. I love the colours from the photos. I like the new business cards. Could you combine the concepts in the business cards from #94 #96 #97
temp web address
http://brightferndesigns.snapvault-host.com/
#89 every thing looks great. A few comments:
1) The business cards - I like the logo side however the information side I prefer earlier designs where you used one block colour ie- #87 or #49. I'm still not sure about this side.
2) The dark black logo square on the paper looks too bold.
Great work. Thanks a lot.
Please check the newly uploaded files.
PANTONES:
Blue: 310 C
Brown: 409 C
Pink: 211 C
Gray: 424 C
FONTS:
Petra: Gotham Medium
Valkenor: Gotham Book
Tagline: Gotham Book
Signature: Custom made
I think I prefer the logo in #52 where it is slightly off the page than #70 where it is completely visible.
I like #70, it's sophisticated however the colour scheme is starting depart from the original and from the style of my work, which I think is not so heavy.
If you have any change or better suggestions please let me know.
Thank you.
#61 - #64 I'm not sure if the dots down the sides are necessary.
My website is down. But I'LL let you know when it's back up so you can take a look at some more pictures. I love the use of them in your designs. So excited by what I'm seeing. Thanks for your work so far.
#57. I love it. Everything adds up perfectly. Not sure about the font. It's a bit clumsy. I'd like something sharper and sleeker.
Great direction.
Does this work for A6
A CD disk is 120 mm in diameter (60 mm radius), with a hole 15 mm diameter (7.5 mm radius)
I'm looking on google for CD dimensions. So far I've found the case cover dimensions:
CD Cover Size Specifications for Printing
The finished dimensions for the outside of printed CD covers are 4.724 inches square. Many printed designs include bleed. The "bleed area" is an extra 1/8" of space for design elements or backgrounds to extend beyond the finished size of your piece. A CD cover with bleeds is printed slightly oversized (4.974 inches square) and then cut down to size, giving the appearance that the printing "bleeds" off the edge of the cover rather than having a white border.
Really like the direction of #51 and #52. Re. #55 I prefer the designs where all embellishments or lines are relevant. What I mean by this is that the curve does not tie in anywhere. It's an additional form that is not part of the logo.
#61 and #62 are great. Can you show me some alternative fonts for the 15% and the brightferndesigns.at
This is fun project! What size should be the CD label be? I am not too sure!
#36 with black background?
I'd be interested to see #34 with black replacing the pink.
I have uploaded information to be included in the flyers and gift certificate.
Please look at my photos to understand my style
http://www.facebook.com/BrightFern.Designs?sk=app_274930158846320

```html
<!DOCTYPE html>
<html lang="en">
<head>
<meta charset="utf-8">
<title>Petra Valkenor – Business Cards</title>
<link rel="stylesheet" href="https://fonts.googleapis.com/css2?family=Montserrat:wght@400;500;600&display=swap">
<style>
  :root {
    --backdrop: #e9e5df;
    --card-black: #0d0d0d;
    --card-white: #ffffff;
    --brand-pink: #e98ab3;
    --brand-gray: #9a9a9d;
    --text-gray: #555555;
    --divider: #cfcfcf;
  }
  * { margin: 0; padding: 0; box-sizing: border-box; }
  html, body {
    width: 1200px; height: 850px; overflow: hidden;
    background: var(--backdrop);
    font-family: "Montserrat", sans-serif;
  }
  .sheet { position: relative; width: 1200px; height: 850px; }

  .card {
    position: absolute;
    box-shadow: 0 6px 18px rgba(0,0,0,0.25);
    overflow: hidden;
  }

  /* Brand lockup */
  .lockup {
    display: flex; flex-direction: column; align-items: center;
  }
  .lockup-mark { display: block; margin-bottom: 12px; }
  .lockup-name {
    font-weight: 400; font-size: 30px; letter-spacing: 2px;
    color: var(--brand-gray);
  }
  .lockup-tagline {
    margin-top: 4px; font-size: 10px; letter-spacing: 5px;
    color: var(--brand-pink); text-transform: uppercase;
  }

  /* Info card (two-tone) */
  .card-info { left: 350px; top: 40px; width: 500px; height: 300px; background: var(--card-white); }
  .card-info .info-band {
    height: 170px; background: var(--card-black);
    display: flex; justify-content: center; align-items: center; padding-top: 6px;
  }
  .card-info .lockup-name { font-size: 28px; color: #bdbdbf; }
  .card-info .info-body {
    display: flex; height: 130px; padding: 26px 28px 0 30px;
  }
  .info-person { width: 220px; }
  .info-person-name {
    font-weight: 600; font-size: 17px; color: var(--brand-pink); margin-bottom: 8px;
  }
  .info-line { font-size: 11px; line-height: 16px; color: var(--text-gray); }
  .info-divider { width: 1px; height: 76px; background: var(--divider); margin: 0 28px 0 0; }
  .info-contact { padding-top: 2px; }
  .info-contact .label { color: var(--brand-pink); margin-right: 4px; }

  /* Logo cards */
  .card-logo-light { left: 80px; top: 430px; width: 480px; height: 290px; background: var(--card-white); }
  .card-logo-dark  { left: 640px; top: 430px; width: 480px; height: 290px; background: var(--card-black); }
  .card-logo-light, .card-logo-dark {
    display: flex; justify-content: center; align-items: center;
  }
  .card-logo-dark .lockup-name { color: #b8b8ba; }
</style>
</head>
<body>
<main class="sheet">

  <section class="card card-info">
    <div class="info-band">
      <div class="lockup">
        <svg class="lockup-mark" width="40" height="40" viewBox="0 0 40 40" aria-hidden="true">
          <circle cx="20" cy="20" r="17" fill="none" stroke="var(--brand-pink)" stroke-width="3"/>
        </svg>
        <span class="lockup-name">Petra Valkenor</span>
        <span class="lockup-tagline">Bright Fern Designs</span>
      </div>
    </div>
    <div class="info-body">
      <div class="info-person">
        <p class="info-person-name">Petra Valkenor</p>
        <p class="info-line">Lindenweg 24/7</p>
        <p class="info-line">1040 Wien</p>
      </div>
      <div class="info-divider"></div>
      <div class="info-contact">
        <p class="info-line"><span class="label">p:</span>06641538206</p>
        <p class="info-line"><span class="label">e:</span>Petra@Valkenor.at</p>
        <p class="info-line">www.BrightFernDesigns.at</p>
      </div>
    </div>
  </section>

  <section class="card card-logo-light">
    <div class="lockup">
      <svg class="lockup-mark" width="50" height="50" viewBox="0 0 50 50" aria-hidden="true">
        <circle cx="25" cy="25" r="21" fill="none" stroke="var(--brand-pink)" stroke-width="3.5"/>
      </svg>
      <span class="lockup-name">Petra Valkenor</span>
      <span class="lockup-tagline">Bright Fern Designs</span>
    </div>
  </section>

  <section class="card card-logo-dark">
    <div class="lockup">
      <svg class="lockup-mark" width="50" height="50" viewBox="0 0 50 50" aria-hidden="true">
        <circle cx="25" cy="25" r="21" fill="none" stroke="var(--brand-pink)" stroke-width="3.5"/>
      </svg>
      <span class="lockup-name">Petra Valkenor</span>
      <span class="lockup-tagline">Bright Fern Designs</span>
    </div>
  </section>

</main>
</body>
</html>
```